Copperfield interiors PTY LTD

My business specializes in commercial fitout which builds walls, ceilings, doors, uses also materials aluminium in works. Id like to have a logo designed for my company too.

Industry/Entity Type

Business

```html
<!DOCTYPE html>
<html lang="en">
<head>
<meta charset="utf-8">
<title>Copperfield Interiors PTY LTD – Business Card</title>
<link rel="stylesheet" href="https://fonts.googleapis.com/css2?family=Michroma&family=Arimo:wght@400;700&display=swap">
<style>
  :root {
    --stage: #2b2b2d;
    --card-dark: #3b3b3e;
    --card-dark-mark: #444448;
    --card-light: #ffffff;
    --ink: #2c2c2e;
    --ink-soft: #6d6d70;
    --rule: #b9b9bc;
    --on-dark: #ffffff;
    --on-dark-soft: #d9d9dc;
  }
  * { margin: 0; padding: 0; box-sizing: border-box; }
  html, body { width: 1200px; height: 880px; overflow: hidden; }
  body {
    background: var(--stage);
    position: relative;
    font-family: "Arimo", Arial, sans-serif;
  }
  .card {
    position: absolute;
    width: 560px;
    height: 320px;
    overflow: hidden;
    box-shadow: 0 14px 30px rgba(0,0,0,.45);
  }

  /* Front side */
  .card-front { left: 130px; top: 80px; background: var(--card-dark); }
  .front-mark {
    position: absolute;
    left: -40px; top: 40px;
    width: 240px; height: 240px;
    border-radius: 50%;
    background: var(--card-dark-mark);
  }
  .front-brand {
    position: absolute;
    left: 160px; top: 110px;
    color: var(--on-dark);
  }
  .brand-name {
    font-family: "Michroma", sans-serif;
    font-size: 30px;
    letter-spacing: 4px;
    line-height: 1;
  }
  .brand-sub {
    font-family: "Michroma", sans-serif;
    font-size: 14px;
    letter-spacing: 5.4px;
    margin-top: 6px;
    color: var(--on-dark-soft);
  }
  .front-web {
    position: absolute;
    left: 0; right: 0; bottom: 44px;
    text-align: center;
    color: var(--on-dark);
    font-size: 13px;
    letter-spacing: 5px;
  }

  /* Back side */
  .card-back { left: 510px; top: 480px; background: var(--card-light); color: var(--ink); }
  .back-brand {
    position: absolute;
    left: 30px; top: 110px;
    display: flex; flex-direction: column; align-items: center;
  }
  .brand-dot {
    width: 56px; height: 56px;
    border-radius: 50%;
    background: var(--ink);
    margin-bottom: 12px;
  }
  .back-brand .brand-name { font-size: 19px; letter-spacing: 3px; color: var(--ink); }
  .back-brand .brand-sub { font-size: 9px; letter-spacing: 3.6px; color: var(--ink-soft); margin-top: 4px; }
  .divider {
    position: absolute;
    left: 282px; top: 64px;
    width: 1px; height: 120px;
    background: var(--rule);
  }
  .contact {
    position: absolute;
    left: 304px; top: 52px;
  }
  .person-name { font-size: 17px; line-height: 1.1; }
  .person-role { font-size: 12px; margin-bottom: 14px; }
  .contact-list { list-style: none; }
  .contact-list li {
    display: flex; align-items: center; gap: 6px;
    font-size: 12.5px; line-height: 1; margin-bottom: 5px;
  }
  .contact-icon { width: 14px; height: 14px; flex: none; }
  .address {
    position: absolute;
    left: 0; right: 0; bottom: 34px;
    text-align: center;
    font-size: 13px;
  }
</style>
</head>
<body>

<section class="card card-front" aria-label="Card front">
  <div class="front-mark"></div>
  <div class="front-brand">
    <div class="brand-name">COPPERFIELD</div>
    <div class="brand-sub">INTERIORS PTY LTD</div>
  </div>
  <div class="front-web">www.copperfieldfitout.com</div>
</section>

<section class="card card-back" aria-label="Card back">
  <div class="back-brand">
    <div class="brand-dot"></div>
    <div class="brand-name">COPPERFIELD</div>
    <div class="brand-sub">INTERIORS PTY LTD</div>
  </div>

  <div class="divider"></div>

  <div class="contact">
    <div class="person-name">LIAM CARTER</div>
    <div class="person-role">Founder</div>
    <ul class="contact-list">
      <li>
        <svg class="contact-icon" viewBox="0 0 14 14" aria-hidden="true">
          <circle cx="7" cy="7" r="7" fill="#2c2c2e"/>
          <path d="M4.3 3.6c.4-.3.8-.2 1 .2l.6 1.1c.2.4 0 .7-.3.9l-.3.2c.3.8 1 1.5 1.8 1.9l.2-.3c.2-.3.5-.5.9-.3l1.1.6c.4.2.5.6.2 1l-.4.5c-.4.5-1 .6-1.6.3C5.7 9 4.8 8 4 6.2c-.3-.6-.2-1.2.3-1.6z" fill="#fff"/>
        </svg>
        (03) 9421 5806
      </li>
      <li>
        <svg class="contact-icon" viewBox="0 0 14 14" aria-hidden="true">
          <circle cx="7" cy="7" r="7" fill="#2c2c2e"/>
          <rect x="3.5" y="4.5" width="7" height="5" fill="none" stroke="#fff" stroke-width="1"/>
          <path d="M3.5 4.5 7 7.3l3.5-2.8" fill="none" stroke="#fff" stroke-width="1"/>
        </svg>
        info@copperfieldfitout.com
      </li>
      <li>
        <svg class="contact-icon" viewBox="0 0 14 14" aria-hidden="true">
          <circle cx="7" cy="7" r="7" fill="#2c2c2e"/>
          <circle cx="7" cy="7" r="3.6" fill="none" stroke="#fff" stroke-width=".9"/>
          <ellipse cx="7" cy="7" rx="1.6" ry="3.6" fill="none" stroke="#fff" stroke-width=".9"/>
          <path d="M3.4 7h7.2" stroke="#fff" stroke-width=".9"/>
        </svg>
        www.copperfieldfitout.com
      </li>
    </ul>
  </div>

  <div class="address">PO BOX 418 Harbour Lane, Docklands Melbourne</div>
</section>

</body>
</html>
```